Inspirational speaker and coach Corinne Valbeck is building a website

Design, Create and launch a 10-15 page Wordpress website. Please research Corinne online and use examples you have access to.

```html
<!DOCTYPE html>
<html lang="en">
<head>
<meta charset="utf-8">
<title>Corinne Valbeck — Speaker &amp; Coach</title>
<link href="https://fonts.googleapis.com/css2?family=Poppins:wght@400;500;600;700&display=swap" rel="stylesheet">
<style>
:root{
  --bg:#131313;
  --bg-alt:#1b1b1b;
  --card:#202020;
  --green:#1fa463;
  --green-dark:#14794a;
  --text:#ffffff;
  --muted:#b5b5b5;
  --line:#2e2e2e;
}
*{box-sizing:border-box;margin:0;padding:0}
html,body{width:1200px;height:4112px;overflow:hidden}
body{background:var(--bg);color:var(--text);font-family:"Poppins",Arial,sans-serif;position:relative}
.abs{position:absolute}
section,header,footer{position:absolute;left:0;width:1200px}
.accent{color:var(--green)}
.btn{position:absolute;display:inline-block;background:var(--green);color:#fff;font-size:14px;font-weight:500;padding:10px 20px;border-radius:4px}
.btn-outline{background:transparent;border:1px solid #555;color:#fff}
.section-title{position:absolute;font-size:34px;font-weight:700}
.section-title::after{content:"";position:absolute;left:0;bottom:-10px;width:60px;height:3px;background:var(--green)}
.center-title::after{left:50%;margin-left:-30px}
.photo{position:absolute}
p{color:var(--muted);font-size:14px;line-height:1.6}

/* header */
.site-header{top:0;height:80px;z-index:3}
.brand{left:160px;top:18px;display:flex;align-items:center;gap:10px;font-weight:700;font-size:16px;line-height:1.1}
.brand-dot{width:36px;height:36px;border-radius:50%;background:var(--green)}
.nav{left:430px;top:28px;display:flex;gap:26px;font-size:14px}
.nav .active{border-bottom:2px solid var(--green);padding-bottom:4px}
.join{left:950px;top:18px;padding:8px 18px}

/* hero */
.hero{top:0;height:620px;background:linear-gradient(90deg,#121212 0%,#1c1c1c 60%,#151515 100%)}
.hero h1{left:160px;top:120px;font-size:42px;line-height:1.25;font-weight:700;width:480px}
.hero .sub{left:160px;top:248px;font-size:20px;color:#fff}
.hero .btn{left:160px;top:340px}
.hero .phone{left:290px;top:346px;display:flex;align-items:center;gap:10px;font-size:16px}
.icon-circle{width:30px;height:30px;border-radius:50%;border:1px solid var(--green);display:flex;align-items:center;justify-content:center}
.hero .photo{left:690px;top:100px;width:370px;height:520px;background:radial-gradient(ellipse at 50% 40%,#8f7a6a 0%,#3a2f2a 45%,#1a1a1a 80%)}
.dot{position:absolute;width:8px;height:8px;border-radius:50%;background:var(--green)}
.slider{left:160px;top:578px;display:flex;gap:8px}
.slider span{width:8px;height:8px;border-radius:50%;background:#555}
.slider span:first-child{background:var(--green)}

/* about */
.about{top:620px;height:500px;background:var(--bg)}
.about .photo{left:160px;top:50px;width:340px;height:350px;border:2px solid var(--green);border-radius:8px;background:linear-gradient(160deg,#a98b6c,#5d4a3c 60%,#2f2a26)}
.about .section-title{left:544px;top:60px}
.about-list{left:544px;top:130px;width:500px;list-style:none}
.about-list li{display:flex;gap:12px;margin-bottom:16px;font-size:13px;color:var(--muted);line-height:1.5}
.about-list li span.ic{flex:none;width:18px;height:18px;border-radius:50%;border:1px solid #888;margin-top:2px}
.about .btn{left:544px;top:355px;font-size:13px;padding:8px 16px}

/* services */
.services{top:1120px;height:520px;background:var(--bg-alt)}
.services .section-title{left:160px;top:50px}
.services .view-all{left:900px;top:54px;font-size:13px;padding:8px 16px}
.svc{position:absolute;top:160px;width:288px;height:272px;background:var(--card);border-radius:8px;border:1px solid var(--line);text-align:center;padding:30px 28px}
.svc.featured{border:2px solid var(--green)}
.svc .svc-icon{width:56px;height:56px;border-radius:50%;background:#2c2c2c;margin:0 auto 14px;display:flex;align-items:center;justify-content:center}
.svc h3{font-size:18px;font-weight:600;margin-bottom:12px}
.svc p{font-size:12px}
.svc .more{display:inline-block;margin-top:16px;font-size:12px;border-bottom:1px solid var(--green);padding-bottom:3px}

/* how it work */
.how{top:1640px;height:500px;background:var(--bg)}
.how .section-title{left:160px;top:140px}
.how .intro{left:160px;top:210px;width:340px;font-size:13px}
.how .btn{left:160px;top:300px;font-size:13px;padding:8px 16px}
.steps{left:600px;top:60px;width:460px}
.step{position:relative;height:104px;padding-left:70px}
.step .num{position:absolute;left:0;top:0;width:48px;height:48px;border-radius:50%;background:var(--green);display:flex;align-items:center;justify-content:center}
.step:not(:last-child) .num::after{content:"";position:absolute;left:23px;top:52px;width:2px;height:50px;background:#3a3a3a}
.step h4{font-size:18px;font-weight:500;margin-bottom:4px}
.step p{font-size:13px;width:360px}

/* together band */
.together{top:2140px;height:400px;background:var(--bg-alt)}
.together .photo{left:0;top:10px;width:500px;height:380px;background:linear-gradient(120deg,#6d5b4c,#a88d74 45%,#3c3b44)}
.together h2{left:540px;top:90px;font-size:30px;font-weight:700;line-height:1.35;width:560px}
.together h3{left:540px;top:190px;font-size:22px;font-weight:500;line-height:1.45;width:560px}
.together .btn{left:540px;top:296px;font-size:13px;padding:8px 16px}

/* why */
.why{top:2540px;height:620px;background:var(--bg)}
.why .section-title{left:0;width:1200px;text-align:center;top:64px}
.why .section-title::after{left:50%}
.reasons{left:160px;top:160px;width:400px;list-style:none}
.reasons li{position:relative;padding-left:50px;height:110px}
.reasons .tick{position:absolute;left:0;top:0;width:30px;height:30px;border-radius:4px;border:1px solid #555;display:flex;align-items:center;justify-content:center}
.reasons li.on .tick{border-color:var(--green)}
.reasons h4{font-size:17px;font-weight:500;margin-bottom:6px}
.reasons li.on h4{color:var(--green)}
.reasons p{font-size:13px}
.request{left:612px;top:140px;width:428px;height:380px;background:#1e2622;border:1px solid #2d3a33;border-radius:8px;padding:26px 30px}
.request h3{text-align:center;font-size:18px;font-weight:600;margin-bottom:20px}
.fields{display:grid;grid-template-columns:1fr 1fr;gap:14px}
.field{font-size:12px;color:var(--muted)}
.field .box{margin-top:6px;height:34px;border-bottom:1px solid #3e4a44}
.field.wide{grid-column:1/3}
.field.wide .box{height:70px}
.request .btn{position:static;display:block;width:110px;margin:24px auto 0;font-size:13px;padding:8px 0;text-align:center}

/* blog */
.blog{top:3160px;height:620px;background:var(--bg-alt)}
.blog .section-title{left:160px;top:40px}
.blog .view-all{left:920px;top:46px;font-size:13px;padding:8px 16px}
.post{position:absolute;top:140px;width:282px;height:380px;background:var(--card);border-radius:8px;border:1px solid var(--line);padding:14px}
.post.featured{border:2px solid var(--green)}
.post .thumb{position:relative;height:170px;border-radius:6px}
.post .date{position:absolute;right:0;top:0;width:40px;height:44px;background:var(--green);font-size:11px;text-align:center;line-height:1.2;padding-top:6px;border-radius:0 6px 0 4px}
.post h4{font-size:16px;font-weight:600;margin:18px 0 8px}
.post p{font-size:12px}
.post .more{display:inline-block;margin-top:14px;font-size:12px;border-bottom:1px solid var(--green);padding-bottom:3px}

/* footer */
.site-footer{top:3780px;height:332px;background:var(--bg)}
.f-col{position:absolute;top:40px}
.f-col h5{font-size:16px;font-weight:600;margin-bottom:16px}
.f-col ul{list-style:none;font-size:13px;color:var(--muted);line-height:1.9}
.f-col ul li::before{content:"› ";color:var(--green)}
.contact li{display:flex;gap:10px;align-items:center;margin-bottom:10px;color:var(--muted);font-size:13px}
.contact li::before{content:none}
.newsletter{display:flex;margin-bottom:16px}
.newsletter .in{width:180px;height:34px;background:#fff;border-radius:3px 0 0 3px}
.newsletter .go{width:36px;height:34px;background:var(--green);border-radius:0 3px 3px 0}
.socials{display:flex;gap:10px}
.socials span{width:30px;height:30px;border:1px solid #555;border-radius:3px}
.copyright{left:0;width:1200px;top:296px;text-align:center;font-size:12px;color:var(--muted);border-top:1px solid var(--line);padding-top:12px}
</style>
</head>
<body>

<section class="hero">
  <div class="dot" style="left:700px;top:130px"></div>
  <div class="dot" style="left:1020px;top:110px"></div>
  <div class="dot" style="left:640px;top:270px;width:6px;height:6px"></div>
  <div class="dot" style="left:1060px;top:330px;width:6px;height:6px"></div>
  <div class="dot" style="left:740px;top:560px;width:6px;height:6px"></div>
  <div class="dot" style="left:980px;top:590px"></div>
  <h1 class="abs">Wanting To Start<br>You Own Business?</h1>
  <div class="abs sub">Get Ready To Pick Up Your Crown</div>
  <a class="btn">Contact Us</a>
  <div class="abs phone">
    <span class="icon-circle"><svg width="14" height="14" viewBox="0 0 24 24" fill="#1fa463"><path d="M6.6 10.8a15.1 15.1 0 0 0 6.6 6.6l2.2-2.2c.3-.3.7-.4 1-.2 1.1.4 2.3.6 3.6.6.6 0 1 .4 1 1V20c0 .6-.4 1-1 1C10.6 21 3 13.4 3 4c0-.6.4-1 1-1h3.5c.6 0 1 .4 1 1 0 1.3.2 2.5.6 3.6.1.3 0 .7-.2 1z"/></svg></span>
    (555) 123 456 789
  </div>
  <div class="photo" role="img" aria-label="Portrait of Corinne Valbeck, smiling, in a dark fringed jacket"></div>
  <div class="abs slider"><span></span><span></span></div>
</section>

<header class="site-header">
  <div class="abs brand"><span class="brand-dot"></span><span>Corinne<br>Valbeck</span></div>
  <nav class="abs nav">
    <span class="active">Home</span><span>About Us</span><span>Services</span><span>How It Work</span><span>Why Choose Us</span><span>Blog</span>
  </nav>
  <a class="btn btn-outline join">Join Us</a>
</header>

<section class="about">
  <div class="photo" role="img" aria-label="Corinne Valbeck holding a small gift in a warm indoor setting"></div>
  <h2 class="section-title">About <span class="accent">Us</span></h2>
  <ul class="abs about-list">
    <li><span class="ic"></span>I am an experienced and seasoned business executive with expertise in operations, administration and management for multimillion dollar companies.</li>
    <li><span class="ic"></span>I possess a strong strategic vision with skills to pinpoint and resolve complex dynamic problems.</li>
    <li><span class="ic"></span>I am particularly focused on organizational structure and balance in helping employees and executives realize their full potential.</li>
    <li><span class="ic"></span>I have a proven track record of sustainably growing company revenue and business development.</li>
  </ul>
  <a class="btn">Read More</a>
</section>

<section class="services">
  <h2 class="section-title">Our <span class="accent">Services</span></h2>
  <a class="btn btn-outline view-all">View All Services</a>
  <div class="svc featured" style="left:160px">
    <div class="svc-icon"><svg width="26" height="26" viewBox="0 0 24 24" fill="none" stroke="#1fa463" stroke-width="2"><circle cx="9" cy="8" r="3"/><path d="M3 20c0-3.3 2.7-6 6-6s6 2.7 6 6"/><path d="M15 5h6v6h-6"/></svg></div>
    <h3>Coaching</h3>
    <p>Lorem Ipsum is simply dummy text of the printing and typesetting industry. Lorem Ipsum has been the industry's</p>
    <span class="more">Learn More ›</span>
  </div>
  <div class="svc" style="left:460px">
    <div class="svc-icon"><svg width="26" height="26" viewBox="0 0 24 24" fill="none" stroke="#1fa463" stroke-width="2"><circle cx="8" cy="9" r="3"/><circle cx="16" cy="9" r="3"/><path d="M2 20c0-3 3-5 6-5s6 2 6 5M12 20c0-3 2-5 4-5s6 2 6 5"/></svg></div>
    <h3>Consulting</h3>
    <p>Lorem Ipsum is simply dummy text of the printing and typesetting industry. Lorem Ipsum has been the industry's</p>
    <span class="more">Learn More ›</span>
  </div>
  <div class="svc" style="left:760px">
    <div class="svc-icon"><svg width="26" height="26" viewBox="0 0 24 24" fill="none" stroke="#1fa463" stroke-width="2"><rect x="3" y="3" width="8" height="8"/><rect x="13" y="3" width="8" height="8"/><rect x="3" y="13" width="8" height="8"/><path d="M13 17h8M17 13v8"/></svg></div>
    <h3>Advisory</h3>
    <p>Lorem Ipsum is simply dummy text of the printing and typesetting industry. Lorem Ipsum has been the industry's</p>
    <span class="more">Learn More ›</span>
  </div>
</section>

<section class="how">
  <h2 class="section-title">How It <span class="accent">Work</span></h2>
  <p class="abs intro">Lorem Ipsum is simply dummy text of the printing and typesetting industry. Lorem Ipsum has been the industry's standard dummy text ever since the.</p>
  <a class="btn btn-outline">Contact Us</a>
  <div class="abs steps">
    <div class="step"><span class="num"><svg width="22" height="22" viewBox="0 0 24 24" fill="none" stroke="#fff" stroke-width="2"><path d="M4 5h16v11H8l-4 4z"/></svg></span><h4>Consultation</h4><p>Lorem Ipsum is simply dummy text of the printing and typesetting industry.</p></div>
    <div class="step"><span class="num"><svg width="22" height="22" viewBox="0 0 24 24" fill="none" stroke="#fff" stroke-width="2"><circle cx="12" cy="7" r="3"/><path d="M12 10v10M8 14h8"/></svg></span><h4>Choose Services</h4><p>Lorem Ipsum is simply dummy text of the printing and typesetting industry. Lorem Ipsum has been the.</p></div>
    <div class="step"><span class="num"><svg width="22" height="22" viewBox="0 0 24 24" fill="none" stroke="#fff" stroke-width="2"><circle cx="8" cy="9" r="3"/><circle cx="16" cy="9" r="3"/><path d="M3 19c0-3 2-5 5-5s5 2 5 5M11 19c0-3 2-5 5-5s5 2 5 5"/></svg></span><h4>Join Meeting</h4><p>Lorem Ipsum is simply dummy text of the printing and typesetting industry. Lorem Ipsum has been the.</p></div>
    <div class="step"><span class="num"><svg width="22" height="22" viewBox="0 0 24 24" fill="none" stroke="#fff" stroke-width="2"><path d="M4 20V10l8-6 8 6v10H4z"/><path d="M10 20v-6h4v6"/></svg></span><h4>Start Your Own Business</h4><p>Lorem Ipsum is simply dummy text of the printing and typesetting industry. Lorem Ipsum has been the.</p></div>
  </div>
</section>

<section class="together">
  <div class="photo" role="img" aria-label="Group selfie of Corinne Valbeck with a smiling community of friends and family"></div>
  <h2 class="abs">No One Can Do This Alone<br>And Succeed!</h2>
  <h3 class="abs">So Find Those That Elevate You Rise<br>Together Better &amp; Faster!</h3>
  <a class="btn btn-outline">Contact Us Today</a>
</section>

<section class="why">
  <h2 class="section-title center-title">Why <span class="accent">Choose Us</span></h2>
  <ul class="abs reasons">
    <li class="on"><span class="tick"><svg width="16" height="16" viewBox="0 0 24 24" fill="none" stroke="#1fa463" stroke-width="3"><path d="M4 12l5 5L20 6"/></svg></span><h4>Lorem Ipsum Dolar</h4><p>Lorem Ipsum is simply dummy text of the printing and typesetting industry. Lorem Ipsum has been the.</p></li>
    <li><span class="tick"><svg width="16" height="16" viewBox="0 0 24 24" fill="none" stroke="#fff" stroke-width="3"><path d="M4 12l5 5L20 6"/></svg></span><h4>Lorem Ipsum Dolar</h4><p>Lorem Ipsum is simply dummy text of the printing and typesetting industry. Lorem Ipsum has been the.</p></li>
    <li><span class="tick"><svg width="16" height="16" viewBox="0 0 24 24" fill="none" stroke="#fff" stroke-width="3"><path d="M4 12l5 5L20 6"/></svg></span><h4>Lorem Ipsum Dolar</h4><p>Lorem Ipsum is simply dummy text of the printing and typesetting industry. Lorem Ipsum has been the.</p></li>
  </ul>
  <div class="abs request">
    <h3>Request For Information</h3>
    <div class="fields">
      <div class="field">First Name<div class="box"></div></div>
      <div class="field">Last Name<div class="box"></div></div>
      <div class="field">Email<div class="box"></div></div>
      <div class="field">Phone<div class="box"></div></div>
      <div class="field wide">Message<div class="box"></div></div>
    </div>
    <a class="btn">Submit Now</a>
  </div>
</section>

<section class="blog">
  <h2 class="section-title">Recent <span class="accent">Blog</span></h2>
  <a class="btn btn-outline view-all">View All Blog</a>
  <article class="post featured" style="left:160px">
    <div class="thumb" role="img" aria-label="Traveller standing on red canyon rocks" style="background:linear-gradient(160deg,#8fb0c8,#b9774c 55%,#6b3d25)"><span class="date">08<br>Jan</span></div>
    <h4>Lorem Ipsum Dolar Sit Amet</h4>
    <p>Lorem Ipsum is simply dummy text of the printing and typesetting industry. Lorem Ipsum has been the industry's.</p>
    <span class="more">Learn More ›</span>
  </article>
  <article class="post" style="left:460px">
    <div class="thumb" role="img" aria-label="Woman by the sea under an open sky" style="background:linear-gradient(180deg,#9fb6cc,#d9d2c6 55%,#5b5048)"><span class="date">08<br>Jan</span></div>
    <h4>Lorem Ipsum Dolar Sit Amet</h4>
    <p>Lorem Ipsum is simply dummy text of the printing and typesetting industry. Lorem Ipsum has been the industry's.</p>
    <span class="more">Learn More ›</span>
  </article>
  <article class="post" style="left:760px">
    <div class="thumb" role="img" aria-label="Speaker at a busy business event" style="background:linear-gradient(150deg,#3d6fb3,#c9b79c 50%,#2b4d3a)"><span class="date">08<br>Jan</span></div>
    <h4>Lorem Ipsum Dolar Sit Amet</h4>
    <p>Lorem Ipsum is simply dummy text of the printing and typesetting industry. Lorem Ipsum has been the industry's.</p>
    <span class="more">Learn More ›</span>
  </article>
</section>

<footer class="site-footer">
  <div class="f-col" style="left:160px;width:180px">
    <div class="brand" style="position:static;margin-bottom:16px"><span class="brand-dot"></span><span>Corinne<br>Valbeck</span></div>
    <p style="font-size:12px">Helping bold founders grow with clarity, courage and a simple plan that turns big ideas into lasting results.</p>
  </div>
  <div class="f-col" style="left:370px">
    <h5>Quick <span class="accent">Links</span></h5>
    <ul><li>Home</li><li>About Us</li><li>Services</li><li>How It Work</li><li>Why Choose Us</li><li>Blog</li><li>Contact Us</li></ul>
  </div>
  <div class="f-col" style="left:540px;width:260px">
    <h5>Contact <span class="accent">Details</span></h5>
    <ul class="contact">
      <li><span class="icon-circle"><svg width="12" height="12" viewBox="0 0 24 24" fill="#1fa463"><path d="M12 2a7 7 0 0 0-7 7c0 5 7 13 7 13s7-8 7-13a7 7 0 0 0-7-7zm0 9.5A2.5 2.5 0 1 1 12 6a2.5 2.5 0 0 1 0 5.5z"/></svg></span>Address Line Come Here<br>Address Line Come Here</li>
      <li><span class="icon-circle"><svg width="12" height="12" viewBox="0 0 24 24" fill="#1fa463"><path d="M6.6 10.8a15.1 15.1 0 0 0 6.6 6.6l2.2-2.2c.3-.3.7-.4 1-.2 1.1.4 2.3.6 3.6.6.6 0 1 .4 1 1V20c0 .6-.4 1-1 1C10.6 21 3 13.4 3 4c0-.6.4-1 1-1h3.5c.6 0 1 .4 1 1 0 1.3.2 2.5.6 3.6.1.3 0 .7-.2 1z"/></svg></span>(555) 123-456-789</li>
      <li><span class="icon-circle"><svg width="12" height="12" viewBox="0 0 24 24" fill="none" stroke="#1fa463" stroke-width="2"><rect x="3" y="5" width="18" height="14"/><path d="M3 6l9 7 9-7"/></svg></span>info@corinnevalbeck.com</li>
    </ul>
  </div>
  <div class="f-col" style="left:830px">
    <h5>Sign Up To <span class="accent">Newsletter</span></h5>
    <div class="newsletter"><span class="in"></span><span class="go"></span></div>
    <div class="socials"><span></span><span></span><span></span><span></span></div>
  </div>
  <div class="abs copyright">Copyright 2021 CorinneValbeck. All Rights Reserved.</div>
</footer>

</body>
</html>
```